Just Listed and Just Sold Post Cards. I have attached copies of what I have had in the past for reference. I have a new company logo attached that needs to be used. Please also include website: www.fernharborfinder.com
email. martawilkes@martawilkeshomes.com
phone 941-555-0173
Target Market(s)
home and land owners
Font styles to use
Sans Serif
Colors
0356a4
Requirements
Must have
- I need a South Gulf Cove Just Listed Card and a Just Sold Card
- Must have My name company name logo website email phone number
- back should read _______. on your block of South Gulf Cove has just SOLD at $________ on _____________________ similar to the one I have attached.
Nice to have
- I like how the attached postcards from before have the shaded picture on the back of the picture on the front. I like to have the aerial as one main photo and the photo with the boat as the other main photo.
- Integrate my Marta Wilkes logo with the TK Meridian logo

```html
<!DOCTYPE html>
<html lang="en">
<head>
<meta charset="utf-8">
<title>South Gulf Cove Just Sold Postcard</title>
<link rel="stylesheet" href="https://fonts.googleapis.com/css2?family=Montserrat:wght@500;700;800&family=Roboto+Condensed:wght@400;700&display=swap">
<style>
  :root {
    --brand-blue: #0356a4;
    --deep-blue: #1d3f8f;
    --ink: #1b1b1b;
    --slate: #6b7280;
    --accent-orange: #e2662a;
    --white: #ffffff;
    --band-light: #f2f3f5;
    --band-mid: #d9dbe0;
    --page: #e9eaec;
  }
  * { box-sizing: border-box; margin: 0; padding: 0; }
  html, body { width: 1200px; height: 1000px; overflow: hidden; }
  body { background: var(--page); font-family: "Roboto Condensed", Arial, sans-serif; color: var(--ink); }

  .canvas { position: relative; width: 1200px; height: 1000px; }

  .postcard {
    position: absolute; left: 255px; width: 690px; height: 460px;
    overflow: hidden; box-shadow: 0 2px 10px rgba(0,0,0,.18);
  }
  .postcard--back { top: 25px; }
  .postcard--front { top: 515px; }

  /* Back side */
  .back-aerial {
    position: absolute; inset: 0;
    background: linear-gradient(180deg, #c9d2ea 0%, #c8d1e4 38%, #b9c3c8 55%, #b3bdab 75%, #a9b29c 100%);
  }
  .back-message { position: absolute; left: 40px; top: 34px; width: 370px; font-size: 13px; line-height: 1.25; }
  .back-message .line { display: flex; align-items: flex-end; gap: 4px; margin-bottom: 14px; }
  .blank { display: inline-block; border-bottom: 1px solid var(--ink); height: 14px; }
  .back-message .closing { font-weight: 700; font-size: 15px; line-height: 1.3; letter-spacing: .2px; }

  .stamp-box { position: absolute; right: 40px; top: 42px; width: 120px; height: 100px; border: 1.5px solid var(--ink); }

  .contact-panel {
    position: absolute; left: 0; top: 212px; width: 320px; height: 118px;
    background: linear-gradient(180deg, var(--white), var(--band-mid));
    border: 2px solid var(--brand-blue); border-left: none; border-top-color: transparent;
    border-radius: 0 14px 14px 0; padding: 14px 18px 0 26px;
  }
  .contact-panel .agent { text-align: center; margin-bottom: 8px; padding-left: 60px; }
  .contact-list { list-style: none; font-weight: 700; font-size: 14.5px; line-height: 1.25; }
  .contact-list li { display: flex; align-items: center; gap: 6px; white-space: nowrap; }
  .contact-list .web { color: var(--brand-blue); }
  .contact-list svg { width: 11px; height: 11px; flex: none; }

  .agent-name {
    display: inline-flex; align-items: center; gap: 6px; white-space: nowrap;
    font-family: "Montserrat", Arial, sans-serif; font-weight: 700;
    color: var(--deep-blue); font-size: 14px; letter-spacing: .5px; text-transform: uppercase;
  }
  .agent-name .mark { width: 14px; height: 14px; border-radius: 50%; background: var(--deep-blue); }
  .agent-title { display: block; font-family: "Montserrat", Arial, sans-serif; font-size: 8px; font-weight: 500; color: var(--accent-orange); letter-spacing: 1px; text-transform: uppercase; }

  /* Front side */
  .front-aerial {
    position: absolute; left: 0; top: 0; width: 690px; height: 330px;
    background: linear-gradient(180deg, #3d6fb8 0%, #6f9fd6 22%, #8aa6bc 34%, #6d8170 52%, #5d7059 72%, #4d6a4c 100%);
  }
  .headline { position: absolute; left: 0; right: 0; top: 48px; text-align: center; color: var(--white); font-family: "Montserrat", Arial, sans-serif; }
  .headline .place { display: block; font-weight: 700; font-size: 20px; letter-spacing: 1.5px; text-shadow: 0 2px 3px rgba(0,0,0,.35); }
  .headline .status { display: block; font-weight: 800; font-size: 84px; line-height: .95; letter-spacing: 2px; text-shadow: 3px 5px 6px rgba(0,0,0,.45); }

  .brand-stripe { position: absolute; left: 0; top: 330px; width: 690px; height: 8px; background: var(--brand-blue); }
  .brand-band { position: absolute; left: 0; top: 338px; width: 690px; height: 122px; background: linear-gradient(180deg, var(--white), var(--band-light) 60%, var(--band-mid)); }
  .brand-band .agent { position: absolute; left: 24px; top: 40px; }
  .brokerage { position: absolute; left: 186px; top: 38px; width: 190px; font-family: "Montserrat", Arial, sans-serif; }
  .brokerage-name { display: inline-flex; align-items: center; gap: 6px; white-space: nowrap; font-weight: 700; font-size: 19px; color: var(--slate); text-transform: uppercase; letter-spacing: .8px; }
  .brokerage-name .mark { width: 15px; height: 15px; background: var(--slate); }
  .brokerage-sub { display: block; font-size: 8.5px; font-weight: 500; color: var(--slate); letter-spacing: 1.2px; text-transform: uppercase; margin-top: 2px; white-space: nowrap; }

  .inset-photo {
    position: absolute; left: 396px; top: 268px; width: 270px; height: 172px;
    background: var(--white); padding: 6px; box-shadow: 0 3px 8px rgba(0,0,0,.35);
  }
  .inset-photo .photo { width: 100%; height: 100%; background: linear-gradient(180deg, #6fa3de 0%, #9cc3ec 38%, #3f6d3c 52%, #5f8fb6 64%, #3d6e99 100%); }
</style>
</head>
<body>
<main class="canvas">

  <section class="postcard postcard--back" aria-label="Postcard back">
    <div class="back-aerial" role="img" aria-label="Faded aerial view of South Gulf Cove canals and coastline"></div>

    <div class="back-message">
      <div class="line"><span class="blank" style="width:330px"></span></div>
      <div class="line" style="padding-left:14px">on your block of South Gulf Cove has just SOLD</div>
      <div class="line">at $<span class="blank" style="width:110px"></span> on <span class="blank" style="width:120px"></span></div>
      <div class="line" style="padding-left:60px">similar to the one I have attached.</div>
      <p class="closing">Please contact me if you are interested in<br>buying or selling property in the area</p>
    </div>

    <div class="stamp-box" aria-label="Stamp area"></div>

    <div class="contact-panel">
      <div class="agent">
        <span class="agent-name"><span class="mark"></span>Marta Wilkes</span>
        <span class="agent-title">Broker Associate</span>
      </div>
      <ul class="contact-list">
        <li class="web">
          <svg viewBox="0 0 12 12"><circle cx="6" cy="6" r="5" fill="none" stroke="#0356a4" stroke-width="1.2"/><path d="M1 6h10M6 1c2 2 2 8 0 10M6 1c-2 2-2 8 0 10" fill="none" stroke="#0356a4" stroke-width=".9"/></svg>
          www.fernharborfinder.com
        </li>
        <li>
          <svg viewBox="0 0 12 12"><rect x="1" y="2.5" width="10" height="7" fill="none" stroke="#0356a4" stroke-width="1.2"/><path d="M1 2.5l5 4 5-4" fill="none" stroke="#0356a4" stroke-width="1.1"/></svg>
          martawilkes@martawilkeshomes.com
        </li>
        <li style="padding-left:40px">
          <svg viewBox="0 0 12 12"><path d="M3 1l2 2.5-1.2 1.3c.7 1.4 1.8 2.5 3.2 3.2L8.3 6.8 11 8.8 9.8 11C5.5 10.6 1.4 6.5 1 2.2z" fill="#0356a4"/></svg>
          941-555-0173
        </li>
      </ul>
    </div>
  </section>

  <section class="postcard postcard--front" aria-label="Postcard front">
    <div class="front-aerial" role="img" aria-label="Aerial photograph of South Gulf Cove with canals, river and the gulf on the horizon"></div>

    <h1 class="headline">
      <span class="place">SOUTH GULF COVE</span>
      <span class="status">JUST SOLD</span>
    </h1>

    <div class="brand-stripe"></div>
    <div class="brand-band">
      <div class="agent">
        <span class="agent-name"><span class="mark"></span>Marta Wilkes</span>
        <span class="agent-title" style="padding-left:20px">Broker Associate</span>
      </div>
      <div class="brokerage">
        <span class="brokerage-name"><span class="mark"></span>TK Meridian</span>
        <span class="brokerage-sub">Tallis-Kemp Realty</span>
      </div>
    </div>

    <figure class="inset-photo">
      <div class="photo" role="img" aria-label="Photograph of a boat cruising a palm-lined canal past waterfront homes"></div>
    </figure>
  </section>

</main>
</body>
</html>
```